Online video and marketing company business cards

Need to get some new business cards designed to fit with our new logo. The cards should be professional, clean and simple.

Cards should have:

Name
Position
2 line address
telephone
mobile
email address
web address

We need to have our logo and if possible say what we do...
ONLINE FILM PRODUCTION & STRATEGY

Marketing

```html
<!DOCTYPE html>
<html lang="en">
<head>
<meta charset="utf-8">
<title>Lumenreel business cards</title>
<link rel="stylesheet" href="https://fonts.googleapis.com/css2?family=Open+Sans:wght@400;600;700&display=swap">
<style>
  :root {
    --navy: #0e4a76;
    --navy-deep: #0a3a5e;
    --sky: #6fa6c8;
    --logo-blue: #3a6fa3;
    --ink-grey: #6b6f73;
    --paper: #ffffff;
    --backdrop: #e9ebee;
  }
  html, body {
    margin: 0;
    width: 1200px;
    height: 1024px;
    overflow: hidden;
    background: var(--backdrop);
    font-family: "Open Sans", Arial, sans-serif;
  }
  .card {
    position: absolute;
    left: 250px;
    width: 700px;
    height: 400px;
    border-radius: 30px;
    overflow: hidden;
    box-shadow: 0 10px 28px rgba(0,0,0,0.18);
  }
  .card-front { top: 70px; background: var(--paper); }
  .card-back { top: 554px; background: var(--navy); }
  .front-band { position: absolute; inset: 0; }
  .brand {
    position: absolute;
    display: flex;
    align-items: center;
    gap: 12px;
    font-weight: 700;
    letter-spacing: -1px;
  }
  .brand-dot {
    width: 30px; height: 30px;
    border-radius: 50%;
    border: 6px solid currentColor;
    box-sizing: border-box;
  }
  .card-front .brand { left: 52px; top: 112px; font-size: 52px; color: var(--logo-blue); }
  .identity { position: absolute; left: 54px; top: 212px; color: var(--ink-grey); }
  .identity-name { font-size: 17px; font-weight: 700; color: var(--navy); text-transform: uppercase; }
  .identity-role { font-size: 15px; font-weight: 600; color: var(--sky); }
  .identity-sep { color: var(--ink-grey); font-weight: 400; margin: 0 4px; }
  .address { margin-top: 6px; font-size: 19px; line-height: 1.3; }
  .divider {
    position: absolute; left: 300px; top: 196px;
    width: 70px; height: 2px; background: #c9ccd0;
  }
  .contact {
    position: absolute; left: 400px; top: 42px;
    list-style: none; margin: 0; padding: 0;
    font-size: 15px; color: var(--ink-grey); line-height: 1.55;
  }
  .contact li { display: flex; align-items: center; gap: 8px; white-space: nowrap; }
  .contact svg { width: 12px; height: 12px; fill: var(--logo-blue); }
  .front-web {
    position: absolute; right: 44px; bottom: 36px;
    color: #fff; font-size: 18px;
  }
  .card-back .brand { left: 196px; top: 150px; font-size: 62px; color: #fff; }
  .back-web {
    position: absolute; left: 200px; top: 244px;
    color: #fff; font-size: 16px;
  }
</style>
</head>
<body>
  <section class="card card-front">
    <svg class="front-band" viewBox="0 0 700 400" preserveAspectRatio="none" aria-hidden="true">
      <path d="M 250 400 C 420 390, 560 280, 640 0 L 700 0 L 700 400 Z" fill="var(--navy)"/>
      <path d="M 280 400 C 450 380, 585 270, 658 0 L 666 0 C 595 280, 462 388, 300 400 Z" fill="var(--sky)"/>
    </svg>
    <div class="brand"><span class="brand-dot"></span>lumenreel</div>
    <div class="identity">
      <div><span class="identity-name">Alex Marlow</span><span class="identity-sep">|</span><span class="identity-role">Job Title</span></div>
      <div class="address">Your Address Goes Here,<br>City, Zip Code, State</div>
    </div>
    <div class="divider"></div>
    <ul class="contact">
      <li><svg viewBox="0 0 12 12"><rect x="1" y="1" width="10" height="10" rx="2"/></svg>00 0 0000 0000</li>
      <li><svg viewBox="0 0 12 12"><path d="M2 1h3l1 3-2 1a7 7 0 0 0 3 3l1-2 3 1v3c0 1-1 1-1 1A10 10 0 0 1 1 2s0-1 1-1z"/></svg>00 0 0000 0000</li>
      <li><svg viewBox="0 0 12 12"><path d="M0 2h12v8H0z M0 2l6 5 6-5" /></svg>name@lumenreel.com</li>
    </ul>
    <div class="front-web">www.lumenreel.com</div>
  </section>

  <section class="card card-back">
    <div class="brand"><span class="brand-dot"></span>lumenreel</div>
    <div class="back-web">www.lumenreel.com</div>
  </section>
</body>
</html>
```